Workers comp/Business Ins/ Payroll- Postcard

I own an insurance agency.  I'm interested in getting some professional advice on how to design a message for what i want to sell.  The products I want to sell are 1) Workers compensation 2) business Insurance 3) Payroll processing. They are integrated together but I'm not sure if it's too much to put on a postcard and if I don't put it on a postcard I could be missing out on sales.
I have the ability to look up what Insurance company a business has their workers compensation  policy with, along with their expiration date.  Based on that information I can tell if the business is overpaying for their Workers compensation. insurance. Most companies are overpaying so I can usually save a company money very quickly if I can get in front of them. Some businesses work with a broker such as myself and buy a policy. When it's done this way, the business ESTIMATES his payroll for the year and at the end of the year they have to complete an audit to find out the actual payroll. Based on audit, they will either owe more money if they were low or get money back if they were high. The other way a business buys a workers comp. policy is with their payroll company. The payroll company will place the policy on Pay -as- you -go which means when you pay your employees every week they  will also calculate how much the workers comp premium is for the week and take that amount out of their checking account. This method avoids large down payments, helps with cash flow and should be very accurate at the end of the policy term.  This is by far the best way to do this for the businessowner. My company also has payroll company and we do this for the insured as well. However, most payroll company's such as QRT and Wagelon charge the customer $15 every time they do this so if it's weekly it is another $780 a year.  We also complete the insured's audit for them which is a big headache for the businessowner.
One of our biggest benefits of doing business with our company is we have a  Steady Rate Forever. When you sign up your base price will never increase. Payroll companies are famous for "discounting a new client" only to increase the rate in a few months later. Our service is also superior to the other payroll companies who use overseas service centers. We have staff within our office and we can answer questions quickly. We usually save businesses money on  their Payroll processing but it's not what we focus on- We focus on the Service.
Business Insurance- One of our main companies that we represent is Brindle Insurance. Brindle is very competitive and we usually write business accounts where we save the business owner money but offer superior coverages.
in summary, I'm offering 1) better workers compensation rates 2) Pay as you go workers comp. 3) Steady Rate, audits done for you, and superior customer service with our payroll company 4) savings on their business insurance with superior coverages.
Sometimes when we talk to an insured we may start with just their payroll and later get the WC and business liability. Each account is different and we do not pressure people to make decisions and we do what is right for them.  The biggest takeaway is we take some things off the plate for the businessowner where they can make just one phone call to get what they need done.  Our Website is www.harbor-mutual.example. my email is tomk@harbor-mutual.example if you have any questions.
Thank You
Tom Kessor

Target Market(s)
Small business owners 1-50 employees
Industry/Entity Type
Insurance and Payroll
Font styles to use
Other font styles liked:
- Let designer choose

Colors
Designer to choose colors to be used in the design.
Requirements
Must have
- It shouldn't be boring- needs to stand out- can use 6x11 inch postcard

Nice to have
- I like humor but not a must

Should not have
- Nothing I can think of

```html
<!DOCTYPE html>
<html lang="en">
<head>
<meta charset="utf-8">
<title>Harbor Mutual Insurance – Postcard</title>
<link rel="stylesheet" href="https://fonts.googleapis.com/css2?family=Montserrat:ital,wght@0,400;0,600;0,700;1,400&family=Noto+Serif:ital,wght@0,600;1,700&display=swap">
<style>
:root{
  --backdrop:#bdbdbd;
  --paper:#ffffff;
  --brand-red:#7d1719;
  --brand-red-light:#9a2a2c;
  --brand-grey:#8b8b8d;
  --band-light:#efefef;
  --ink:#2b2b2b;
  --photo-light:#e9ecef;
  --photo-mid:#b8c0c8;
  --photo-dark:#2a3342;
  --sky:#6f9ab8;
}
*{margin:0;padding:0;box-sizing:border-box}
html,body{width:750px;height:1200px;overflow:hidden}
body{background:var(--backdrop);font-family:"Montserrat",Arial,sans-serif;color:var(--ink);position:relative}
.postcard{position:absolute;left:45px;width:660px;height:359px;background:var(--paper);overflow:hidden;box-shadow:0 6px 14px rgba(0,0,0,.28)}
.postcard--front{top:200px}
.postcard--back{top:640px}
.abs{position:absolute}
.brand-name{font-family:"Noto Serif",Georgia,serif;font-weight:600;color:var(--brand-red);text-align:center;line-height:1.05;letter-spacing:.5px}
.postcard--front .brand-name{left:20px;top:42px;width:290px;font-size:30px}
.postcard--back .brand-name{left:382px;top:30px;width:160px;font-size:16px}
.photo-desk{left:300px;top:0;width:360px;height:171px;background:linear-gradient(100deg,var(--photo-light) 0%,#f4f5f7 35%,var(--photo-mid) 70%,var(--photo-dark) 100%)}
.headline-band{left:0;top:133px;width:331px;height:100px;background:linear-gradient(90deg,var(--brand-red) 60%,var(--brand-red-light));padding:11px 0 0 36px}
.headline{font-family:"Noto Serif",Georgia,serif;font-style:italic;font-weight:700;color:#fff;font-size:23px;line-height:24px;list-style:none}
.headline li{position:relative}
.headline li::before{content:"";position:absolute;left:-12px;top:11px;width:4px;height:4px;border-radius:50%;background:#c8474a}
.copy{font-size:8.6px;line-height:10.5px}
.copy b{font-weight:700}
.front-intro{left:37px;top:245px;width:298px}
.front-detail{left:351px;top:196px;width:296px}
.front-detail p+p{margin-top:10px}
.front-band{left:0;top:0}
.front-url{left:44px;top:323px;font-size:13.5px;color:#fff;letter-spacing:1px;font-weight:400;white-space:nowrap}
.front-url b{font-weight:700}
.photo-towers{left:0;top:0;width:332px;height:79px;background:linear-gradient(180deg,var(--sky) 0%,#9fc0d6 45%,var(--photo-dark) 100%)}
.back-intro{left:37px;top:90px;width:300px}
.summary-band{left:0;top:184px;width:380px;height:80px;background:var(--band-light)}
.summary{left:37px;top:196px;width:300px}
.summary .accent{color:var(--brand-red);font-weight:700}
.summary ol{list-style:none}
.summary li{display:flex;align-items:center;gap:4px}
.num{display:inline-block;width:7px;height:7px;border-radius:50%;background:var(--brand-red);color:#fff;font-size:5px;line-height:7px;text-align:center;font-weight:700}
.takeaway{left:37px;top:275px;width:270px}
.footer-band{left:0;top:311px;width:330px;height:48px;background:var(--brand-grey)}
.contact{top:319px;color:#fff;white-space:nowrap}
.contact .label{font-size:6px;line-height:8px}
.contact .value{font-size:7px;font-weight:700;line-height:11px;display:flex;align-items:center;gap:3px}
.contact .note{font-size:4.5px;font-style:italic;padding-left:11px}
.contact--web{left:30px}
.contact--mail{left:168px}
.stamp-box{left:572px;top:20px;width:64px;height:63px;background:var(--brand-grey)}
</style>
</head>
<body>

<section class="postcard postcard--front" aria-label="Postcard front">
  <div class="abs photo-desk" role="img" aria-label="Photo of hands reviewing paperwork with a pen beside a laptop"></div>
  <div class="abs brand-name">Harbor Mutual<br>Insurance</div>

  <div class="abs headline-band">
    <ul class="headline">
      <li>Workers Compensation</li>
      <li>Business Insurance</li>
      <li>Payroll Processing.</li>
    </ul>
  </div>

  <p class="abs copy front-intro">I have the ability to look up what Insurance company a business has their <b>workers compensation policy</b> with, along with their expiration date. Based on that information I can tell if the business is overpaying for their <b>Workers compensation. insurance.</b> Most companies are overpaying so I can usually <b>save a company money very quickly</b> if I can get in front of them.</p>

  <div class="abs copy front-detail">
    <p>The other way a business buys a workers comp. policy is with their <b>payroll company.</b> The payroll company will place the policy on Pay -as- you -go which means when you pay your employees every week they will also calculate how much the workers comp premium is for the week and take that amount out of their checking account. This method <b>avoids large down payments, helps with cash flow</b> and should be <b>very accurate</b> at the end of the policy term. This is by far the best way to do this for the businessowner. most payroll company's such as <b>QRT and Wagelon</b> charge the customer <b>$15</b> every time they do this so if it's weekly it is another <b>$780 a year.</b></p>
    <p>We also complete the insured's audit for them which is a big headache for the businessowner.</p>
  </div>

  <svg class="abs front-band" width="660" height="359" viewBox="0 0 660 359" aria-hidden="true">
    <polygon points="0,314 322,314 333,359 0,359" fill="var(--brand-grey)"/>
    <polygon points="333,348 566,348 571,359 338,359" fill="var(--brand-grey)"/>
    <polygon points="576,348 660,348 660,359 581,359" fill="var(--brand-red)"/>
  </svg>
  <div class="abs front-url">www.<b>harbor-mutual</b>.example</div>
</section>

<section class="postcard postcard--back" aria-label="Postcard back">
  <div class="abs photo-towers" role="img" aria-label="Photo looking up at glass office towers against a cloudy sky"></div>
  <div class="abs summary-band"></div>

  <svg class="abs" width="660" height="359" viewBox="0 0 660 359" aria-hidden="true">
    <polygon points="332,0 334,0 400,180 334,359 332,359 332,0" fill="var(--paper)"/>
    <polygon points="308,0 324,0 392,180 324,359 306,359 374,180" fill="var(--brand-red)"/>
    <polygon points="334,0 354,0 418,180 348,359 330,359 398,180" fill="var(--brand-grey)"/>
  </svg>

  <p class="abs copy back-intro">One of our biggest benefits of doing business with our company is we have a <b>Steady Rate Forever.</b> When you sign up your base <b>price will never increase.</b> Payroll companies are famous for <b>"discounting a new client"</b> only to increase the rate in a few months later. Our service is also superior to the other payroll companies who use overseas service centers. We have staff within our office and we can answer questions quickly. We usually save businesses money on their Payroll processing but it's not what we focus on- We focus on the Service.</p>

  <div class="abs copy summary">
    <p>in summary, <span class="accent">I'm offering</span></p>
    <ol>
      <li><span class="num">1</span>better workers compensation rates</li>
      <li><span class="num">2</span>Pay as you go workers comp.</li>
      <li><span class="num">3</span>Steady Rate, audits done for you, and superior customer service</li>
      <li><span class="num">4</span>with our payroll company</li>
      <li><span class="num">5</span>savings on their business insurance with superior coverages.</li>
    </ol>
  </div>

  <p class="abs copy takeaway">The biggest takeaway is we take some things off the plate for the businessowner where they can make just one phone call to get what they need done.</p>

  <div class="abs footer-band"></div>
  <svg class="abs" width="660" height="359" viewBox="0 0 660 359" aria-hidden="true">
    <polygon points="320,311 330,311 306,359 296,359" fill="var(--brand-red)"/>
  </svg>
  <div class="abs contact contact--web">
    <p class="label">Our Website is</p>
    <p class="value">
      <svg width="8" height="8" viewBox="0 0 10 10" aria-hidden="true"><circle cx="5" cy="5" r="4.3" fill="none" stroke="#fff" stroke-width="1"/><path d="M.7 5h8.6M5 .7c-2.2 2.5-2.2 6.1 0 8.6M5 .7c2.2 2.5 2.2 6.1 0 8.6" fill="none" stroke="#fff" stroke-width=".8"/></svg>
      www.harbor-mutual.example.
    </p>
  </div>
  <div class="abs contact contact--mail">
    <p class="label">my email is</p>
    <p class="value">
      <svg width="8" height="8" viewBox="0 0 10 10" aria-hidden="true"><circle cx="5" cy="5" r="4.3" fill="none" stroke="#fff" stroke-width="1"/><rect x="2.6" y="3.4" width="4.8" height="3.4" fill="none" stroke="#fff" stroke-width=".7"/><path d="M2.6 3.4 5 5.3 7.4 3.4" fill="none" stroke="#fff" stroke-width=".7"/></svg>
      tomk@harbor-mutual.example
    </p>
    <p class="note">if you have any questions</p>
  </div>

  <div class="abs brand-name">Harbor Mutual<br>Insurance</div>
  <div class="abs stamp-box" aria-hidden="true"></div>
</section>

</body>
</html>
```